Skyreach Northern Flights
Private Charters
Skyreach Northern Flights  - Aviation
Creative Brief
Cutting-Edge
Tamara Holbrook
Business Development
5127 N. Darrow, Suite 240 Scottsdale, AZ 85254
tholbrook@skyreachnorthernflights.example
www.skyreachnorthernflights.example

```html
<!DOCTYPE html>
<html lang="en">
<head>
<meta charset="utf-8">
<title>Skyreach Northern Flights – Stationery</title>
<link href="https://fonts.googleapis.com/css2?family=Cormorant+Garamond:wght@600&family=Open+Sans:wght@400;600&display=swap" rel="stylesheet">
<style>
  :root {
    --backdrop: #e6e6e6;
    --paper: #ffffff;
    --brand-brown: #6b3b1f;
    --ink: #3a3a3a;
    --ink-soft: #7a7a7a;
    --gold-deep: #e2c300;
    --gold-light: #f7eb7a;
    --rule-dark: #333333;
  }
  * { box-sizing: border-box; margin: 0; padding: 0; }
  html, body { width: 1200px; height: 854px; overflow: hidden; }
  body {
    background: var(--backdrop);
    font-family: "Open Sans", Arial, sans-serif;
    color: var(--ink);
    position: relative;
  }
  .sheet {
    position: absolute;
    background: var(--paper);
    box-shadow: 0 1px 3px rgba(0,0,0,.18);
    overflow: hidden;
  }
  .brand {
    font-family: "Cormorant Garamond", Georgia, serif;
    font-weight: 600;
    color: var(--brand-brown);
    text-transform: uppercase;
    letter-spacing: .04em;
    line-height: 1.05;
    display: flex;
    align-items: center;
    gap: 8px;
  }
  .brand-mark {
    width: 12px; height: 12px;
    background: var(--brand-brown);
    flex: none;
  }
  .brand-name { display: block; }
  .gold-strip {
    position: absolute;
    left: 0; right: 0; bottom: 0;
    background: linear-gradient(90deg, var(--gold-deep), var(--gold-light) 60%, var(--gold-deep));
  }
  .strip-web {
    position: absolute;
    right: 14px;
    font-size: 6px;
    color: var(--ink-soft);
  }
  .contact {
    position: absolute;
    border-left: 2px solid var(--rule-dark);
    padding-left: 5px;
    font-size: 6px;
    line-height: 1.45;
    color: var(--ink);
  }

  /* Letterhead */
  .letterhead { left: 65px; top: 34px; width: 487px; height: 782px; }
  .letterhead .brand { position: absolute; left: 48px; top: 34px; font-size: 17px; }
  .letterhead .contact { left: 10px; bottom: 22px; }
  .letterhead .gold-strip { height: 14px; }
  .letterhead .strip-web { bottom: 17px; }

  /* Business cards */
  .card-front { left: 600px; top: 62px; width: 211px; height: 125px; border-radius: 7px; }
  .card-front .brand { position: absolute; left: 14px; top: 12px; font-size: 9px; gap: 5px; }
  .card-front .brand-mark { width: 7px; height: 7px; }
  .card-front .person { position: absolute; right: 14px; top: 36px; text-align: right; }
  .card-front .person-name { font-size: 7px; font-weight: 600; color: var(--ink); }
  .card-front .person-role { font-size: 5px; color: var(--ink-soft); }
  .card-front .contact { left: 6px; top: 42px; font-size: 5px; border-left-width: 1.5px; }
  .card-front .gold-strip { height: 8px; }
  .card-front .strip-web { bottom: 10px; right: 8px; font-size: 4.5px; }

  .card-back {
    left: 833px; top: 62px; width: 211px; height: 125px; border-radius: 7px;
    background: radial-gradient(ellipse at center, var(--gold-light), var(--gold-deep) 80%);
    display: flex; align-items: center; justify-content: center;
  }
  .card-back .brand { color: var(--paper); font-size: 11px; gap: 6px; }
  .card-back .brand-mark { background: var(--paper); width: 8px; height: 8px; }

  /* Envelope front */
  .envelope-front { left: 595px; top: 218px; width: 552px; height: 288px; }
  .envelope-front .brand { position: absolute; left: 48px; top: 20px; font-size: 14px; }
  .envelope-front .contact { left: 6px; top: 206px; font-size: 5.5px; }
  .envelope-front .gold-strip { height: 10px; }
  .envelope-front .strip-web { bottom: 12px; }

  /* Envelope back */
  .envelope-back { left: 595px; top: 523px; width: 552px; height: 293px; }
  .envelope-back .flap { position: absolute; left: 0; top: 0; width: 552px; height: 110px; }
  .envelope-back .brand {
    position: absolute; left: 0; right: 0; top: 24px;
    justify-content: center; font-size: 14px;
  }
</style>
</head>
<body>

<section class="sheet letterhead" aria-label="Letterhead">
  <div class="brand"><span class="brand-mark"></span><span class="brand-name">Skyreach Northern<br>Flights</span></div>
  <address class="contact">
    5127 N. Darrow, Suite 240<br>
    Scottsdale, AZ 85254<br>
    Toll free: 800 555 0190<br>
    Phone: 480 555 0142<br>
    Fax: 480 555 0143<br>
    Email: tholbrook@skyreachnorthernflights.example
  </address>
  <span class="strip-web">www.skyreachnorthernflights.example</span>
  <div class="gold-strip"></div>
</section>

<section class="sheet card-front" aria-label="Business card front">
  <div class="brand"><span class="brand-mark"></span><span class="brand-name">Skyreach Northern<br>Flights</span></div>
  <div class="person">
    <div class="person-name">Tamara Holbrook</div>
    <div class="person-role">Business Development</div>
  </div>
  <address class="contact">
    5127 N. Darrow, Suite 240<br>
    Scottsdale, AZ 85254<br>
    Toll free: 800 555 0190<br>
    Phone: 480 555 0142<br>
    Mobile: 480 555 0144<br>
    Fax: 480 555 0143<br>
    tholbrook@skyreachnorthernflights.example
  </address>
  <span class="strip-web">www.skyreachnorthernflights.example</span>
  <div class="gold-strip"></div>
</section>

<section class="sheet card-back" aria-label="Business card back">
  <div class="brand"><span class="brand-mark"></span><span class="brand-name">Skyreach Northern<br>Flights</span></div>
</section>

<section class="sheet envelope-front" aria-label="Envelope front">
  <div class="brand"><span class="brand-mark"></span><span class="brand-name">Skyreach Northern<br>Flights</span></div>
  <address class="contact">
    5127 N. Darrow, Suite 240<br>
    Scottsdale, AZ 85254<br>
    Toll free: 800 555 0190<br>
    Phone: 480 555 0142<br>
    Fax: 480 555 0143<br>
    Email: tholbrook@skyreachnorthernflights.example
  </address>
  <span class="strip-web">www.skyreachnorthernflights.example</span>
  <div class="gold-strip"></div>
</section>

<section class="sheet envelope-back" aria-label="Envelope back">
  <svg class="flap" viewBox="0 0 552 110" aria-hidden="true">
    <defs>
      <linearGradient id="flapGold" x1="0" x2="1" y1="0" y2="0">
        <stop offset="0" stop-color="var(--gold-deep)"/>
        <stop offset=".5" stop-color="var(--gold-light)"/>
        <stop offset="1" stop-color="var(--gold-deep)"/>
      </linearGradient>
    </defs>
    <path d="M0 0 H552 V14 L510 104 Q506 110 498 110 H54 Q46 110 42 104 L0 14 Z" fill="url(#flapGold)"/>
  </svg>
  <div class="brand"><span class="brand-mark"></span><span class="brand-name">Skyreach Northern<br>Flights</span></div>
</section>

</body>
</html>
```